Tech business card design

We need an amazing business card design for our new business 'Brakka' a marketing tech startup based in Sydney, Australia. We provide an online marketplace for businesses to search and buy advertising media, connect with service providers and learn more about marketing. We wish to communicate 'cool tech', reliability and professionalism and design based around our logo.

Target Market(s)

Business Owners

Contact Information for Business Card

Name
Position
Email Address
Website
Phone Number

Font styles to use
Other font styles liked:
• Avenir & Avenir Next

Colors

Designer to choose colors to be used in the design.

```html
<!DOCTYPE html>
<html lang="en">
<head>
<meta charset="utf-8">
<title>Brakka Business Card</title>
<link href="https://fonts.googleapis.com/css2?family=Roboto:wght@400;500;900&display=swap" rel="stylesheet">
<style>
  :root {
    --navy: #12133d;
    --navy-soft: #1c1e55;
    --white: #ffffff;
    --muted: #c9cbe6;
    --backdrop: #b9b9b9;
    --backdrop-light: #dcdcdc;
  }
  html, body {
    margin: 0;
    padding: 0;
    overflow: hidden;
  }
  .canvas {
    position: relative;
    width: 1200px;
    height: 930px;
    overflow: hidden;
    background: radial-gradient(ellipse at 50% 45%, var(--backdrop-light), var(--backdrop) 75%);
    font-family: "Roboto", Arial, sans-serif;
  }
  .card {
    position: absolute;
    width: 560px;
    height: 320px;
    border-radius: 22px;
    overflow: hidden;
    box-shadow: 0 10px 24px rgba(0, 0, 0, 0.25);
  }
  .card-back {
    left: 90px;
    top: 110px;
    background: var(--navy);
    display: flex;
    align-items: center;
    justify-content: center;
  }
  .card-front {
    left: 550px;
    top: 500px;
    background: var(--navy);
  }
  .card-front .curve {
    position: absolute;
    inset: 0;
  }
  .wordmark {
    font-weight: 900;
    letter-spacing: -2px;
    line-height: 1;
  }
  .card-back .wordmark {
    color: var(--white);
    font-size: 96px;
  }
  .card-front .wordmark {
    position: absolute;
    right: 40px;
    top: 36px;
    color: var(--navy);
    font-size: 72px;
  }
  .contact {
    position: absolute;
    left: 40px;
    bottom: 30px;
    color: var(--white);
  }
  .contact .name {
    font-size: 19px;
    font-weight: 500;
    margin: 0;
  }
  .contact .role {
    font-size: 12px;
    color: var(--muted);
    margin: 2px 0 12px;
  }
  .contact .address {
    font-size: 12px;
    color: var(--muted);
    margin: 0 0 10px;
    line-height: 1.35;
    font-style: normal;
  }
  .contact ul {
    list-style: none;
    margin: 0;
    padding: 0;
  }
  .contact li {
    display: flex;
    align-items: center;
    gap: 8px;
    font-size: 12px;
    line-height: 1.5;
  }
  .contact li svg {
    width: 10px;
    height: 10px;
    fill: none;
    stroke: var(--white);
    stroke-width: 1.6;
  }
</style>
</head>
<body>
<div class="canvas">
  <section class="card card-back">
    <span class="wordmark">brakka</span>
  </section>

  <section class="card card-front">
    <svg class="curve" viewBox="0 0 560 320" aria-hidden="true">
      <path d="M150 0 Q300 228 560 236 L560 0 Z" fill="var(--white)"/>
      <path d="M118 0 Q285 252 560 254" fill="none" stroke="var(--white)" stroke-width="3"/>
    </svg>
    <span class="wordmark">brakka</span>
    <div class="contact">
      <p class="name">Daniel Hart</p>
      <p class="role">Director</p>
      <address class="address">218 Kent Lane<br>Sydney, NSW 2000</address>
      <ul>
        <li>
          <svg viewBox="0 0 10 10"><path d="M2 1 L4 3 L3 4 Q4 6 6 7 L7 6 L9 8 L8 9 Q3 9 1 2 Z"/></svg>
          +61 2 8015 3392
        </li>
        <li>
          <svg viewBox="0 0 10 10"><rect x="1" y="2" width="8" height="6"/><path d="M1 2 L5 5.5 L9 2"/></svg>
          info@brakka.com
        </li>
        <li>
          <svg viewBox="0 0 10 10"><circle cx="5" cy="5" r="4"/><path d="M1 5 H9 M5 1 Q2.5 5 5 9 M5 1 Q7.5 5 5 9"/></svg>
          www.brakka.com
        </li>
      </ul>
    </div>
  </section>
</div>
</body>
</html>
```